Clear Meadow Cleaning Services - New Brochure Design Project

Need a very good and polished Brochure from my Commercial Cleaning Services business. I have attached what I have done in the past. Need to take to the next level . Something that will compliment my website .https://quentin-v.sitenook.example/

Target Market(s)

Business /Schools/Churches/ Just about any non-residential establishment

Requirements
Must have
• Professional / Polished look and feel

```html
<!DOCTYPE html>
<html lang="en">
<head>
<meta charset="utf-8">
<title>Clear Meadow Cleaning Services – Brochure Outside</title>
<link href="https://fonts.googleapis.com/css2?family=Open+Sans:ital,wght@0,400;0,600;0,700;1,400&family=Oswald:wght@500&family=Luckiest+Guy&display=swap" rel="stylesheet">
<style>
  :root {
    --navy: #1f2c5c;
    --navy-deep: #16224a;
    --green: #5fae3c;
    --lime: #8fc440;
    --cyan: #1ba3d8;
    --ink: #1d1d1d;
    --quote-mark: #5b6b99;
    --paper: #f7f8fa;
    --stage: #2a2a2a;
    --photo-warm: #c9b89a;
    --photo-cool: #8e9aa5;
  }
  * { box-sizing: border-box; margin: 0; padding: 0; }
  html, body { width: 802px; height: 1200px; overflow: hidden; }
  body { background: var(--stage); font-family: "Open Sans", Arial, sans-serif; color: var(--ink); }

  .brochure { position: absolute; left: 21px; top: 305px; width: 760px; height: 590px; display: flex; box-shadow: 0 6px 24px rgba(0,0,0,.5); }
  .panel { position: relative; width: 253.34px; height: 590px; background: var(--paper); overflow: hidden; text-align: center; }
  .abs { position: absolute; left: 0; right: 0; }

  .footer { position: absolute; left: 0; right: 0; bottom: 0; height: 34px; background: linear-gradient(180deg, var(--navy) 0%, var(--navy-deep) 100%); color: #fff; font-size: 8.5px; letter-spacing: .8px; line-height: 31px; border-top: 3px solid #9aa6c4; }
  .footer--lime { background: var(--lime); border-top-color: #b8d98a; }

  .brand { font-size: 15px; font-weight: 600; color: var(--navy); line-height: 1.1; display: inline-flex; align-items: center; gap: 6px; text-align: left; }
  .brand-dot { width: 14px; height: 14px; border-radius: 50%; background: var(--cyan); flex: none; }
  .brand-sub { font-family: "Open Sans", Arial, sans-serif; font-size: 9px; font-weight: 400; color: var(--green); display: block; margin-top: 3px; }

  /* left panel */
  .welcome-title { top: 22px; font-weight: 700; font-size: 19px; line-height: 1.15; color: var(--navy); }
  .welcome-title span { color: var(--green); display: block; }
  .benefits { top: 82px; left: 30px; right: 14px; list-style: none; text-align: left; font-size: 10px; }
  .benefits li { display: flex; gap: 8px; margin-bottom: 6px; line-height: 1.3; }
  .benefits svg { flex: none; margin-top: 1px; }
  .quote-call { top: 178px; font-family: "Luckiest Guy", "Open Sans", sans-serif; color: var(--cyan); font-size: 12px; letter-spacing: .5px; line-height: 1.3; }
  .quote-call span { display: block; color: var(--green); font-size: 17px; }
  .left-brand { top: 232px; }
  .left-brand .brand { font-size: 10.5px; }
  .left-brand .brand-dot { width: 10px; height: 10px; }
  .contact-icons { top: 281px; display: flex; justify-content: center; gap: 8px; }
  .contact-lines { top: 304px; font-size: 10px; line-height: 1.75; }
  .photo { position: absolute; left: 0; right: 0; }
  .left-photo { top: 355px; height: 201px; background: linear-gradient(135deg, #6b7784 0%, #b9a86a 45%, #d8c34a 60%, #7d8a96 100%); }
  .eoe { top: 515px; color: #fff; font-size: 10px; font-weight: 600; line-height: 1.4; text-shadow: 0 1px 2px rgba(0,0,0,.6); }

  /* middle panel */
  .middle { background: var(--navy); }
  .testimonial { position: absolute; left: 26px; right: 26px; border: 1px dashed #6b7aa8; border-radius: 8px; padding: 18px 12px 9px; color: #e9ecf5; font-style: italic; font-size: 8.5px; line-height: 1.4; }
  .testimonial .mark { position: absolute; top: -15px; left: 0; right: 0; height: 28px; display: flex; justify-content: center; }
  .testimonial .mark svg { background: var(--navy); padding: 0 6px; box-sizing: content-box; }
  .testimonial .who { display: block; margin-top: 7px; font-weight: 700; color: var(--cyan); font-size: 9.5px; line-height: 1.3; }
  .testimonial .where { display: block; font-style: normal; color: var(--green); font-size: 8.5px; line-height: 1.3; }
  .t1 { top: 38px; }
  .t2 { top: 172px; }
  .middle-lower { position: absolute; left: 0; right: 0; top: 298px; height: 292px; }
  .middle-brand { top: 348px; }
  .queries { top: 404px; font-size: 12px; line-height: 1.5; }
  .queries strong { display: block; color: var(--green); font-size: 15px; }
  .queries strong em { font-style: normal; color: var(--cyan); }
  .icon-row { display: flex; justify-content: center; }
  .address { top: 478px; font-size: 10.5px; line-height: 1.45; }
  .middle-phone { top: 527px; font-size: 10.5px; }

  /* right panel */
  .cover-brand { top: 24px; }
  .cover-brand .brand { font-size: 17px; }
  .cover-brand .brand-dot { width: 18px; height: 18px; }
  .tagline { top: 100px; color: var(--cyan); font-size: 11.5px; font-weight: 600; }
  .cover-photo { top: 128px; height: 260px; background: linear-gradient(160deg, #d9dfe3 0%, var(--photo-cool) 35%, var(--photo-warm) 60%, #6e7682 100%); }
  .banner { position: absolute; left: 36px; right: 36px; top: 378px; height: 64px; background: var(--navy); border-radius: 0 0 10px 10px; color: #fff; font-family: "Oswald", sans-serif; font-weight: 500; font-size: 19px; line-height: 1.22; padding-top: 7px; letter-spacing: .3px; }
  .about { top: 448px; left: 18px; right: 18px; font-size: 7.6px; line-height: 1.4; }
  .call-us { top: 500px; font-family: "Luckiest Guy", "Open Sans", sans-serif; color: var(--cyan); font-size: 14px; letter-spacing: .5px; }
  .big-phone { top: 516px; display: flex; justify-content: center; align-items: center; gap: 6px; font-size: 25px; font-weight: 700; color: var(--navy); }
</style>
</head>
<body>
<main class="brochure">

  <!-- Panel: inside flap -->
  <section class="panel panel--welcome">
    <h2 class="abs welcome-title">WE ARE HERE<span>FOR YOU!</span></h2>
    <ul class="abs benefits">
      <li><svg width="11" height="11" viewBox="0 0 12 12"><circle cx="6" cy="6" r="6" fill="var(--green)"/><polyline points="3,6.2 5.2,8.3 9,4" fill="none" stroke="#fff" stroke-width="1.6"/></svg>We're Thorough - We're Reliable</li>
      <li><svg width="11" height="11" viewBox="0 0 12 12"><circle cx="6" cy="6" r="6" fill="var(--green)"/><polyline points="3,6.2 5.2,8.3 9,4" fill="none" stroke="#fff" stroke-width="1.6"/></svg>We're Affordable</li>
      <li><svg width="11" height="11" viewBox="0 0 12 12"><circle cx="6" cy="6" r="6" fill="var(--green)"/><polyline points="3,6.2 5.2,8.3 9,4" fill="none" stroke="#fff" stroke-width="1.6"/></svg>We Guarantee Our Work</li>
      <li><svg width="11" height="11" viewBox="0 0 12 12"><circle cx="6" cy="6" r="6" fill="var(--green)"/><polyline points="3,6.2 5.2,8.3 9,4" fill="none" stroke="#fff" stroke-width="1.6"/></svg>Licensed and Insured for your protection</li>
    </ul>
    <p class="abs quote-call">Please Call for a<span>Free Quote Today:</span></p>
    <div class="abs left-brand"><span class="brand"><i class="brand-dot"></i><span>Clear Meadow<br>Cleaning Services</span></span></div>
    <div class="abs contact-icons">
      <svg width="16" height="16" viewBox="0 0 16 16"><circle cx="8" cy="8" r="8" fill="var(--green)"/><path d="M5.3 4.3l1.4-.3.8 2-1 .7c.4 1 1.2 1.8 2.2 2.2l.7-1 2 .8-.3 1.4c-3 .3-6-2.7-5.8-5.8z" fill="#fff"/></svg>
      <svg width="16" height="16" viewBox="0 0 16 16"><circle cx="8" cy="8" r="8" fill="var(--green)"/><rect x="4.3" y="5.3" width="7.4" height="5.4" fill="none" stroke="#fff" stroke-width="1"/><polyline points="4.3,5.5 8,8.3 11.7,5.5" fill="none" stroke="#fff" stroke-width="1"/></svg>
      <svg width="16" height="16" viewBox="0 0 16 16"><circle cx="8" cy="8" r="8" fill="var(--green)"/><circle cx="8" cy="8" r="3.8" fill="none" stroke="#fff" stroke-width="1"/><ellipse cx="8" cy="8" rx="1.6" ry="3.8" fill="none" stroke="#fff" stroke-width=".9"/><line x1="4.2" y1="8" x2="11.8" y2="8" stroke="#fff" stroke-width=".9"/></svg>
    </div>
    <p class="abs contact-lines">555.014.7290<br>quentin@clearmeadowclean.example<br>www.clearmeadowcleanings.example</p>
    <div class="photo left-photo" role="img" aria-label="Photo of yellow-gloved hands holding a blue cloth and a spray bottle"></div>
    <svg class="abs" style="top:340px" width="254" height="50" viewBox="0 0 254 50" aria-hidden="true">
      <path d="M0 40 Q120 30 254 0 L254 0 L0 0 Z" fill="var(--paper)"/>
      <path d="M0 40 Q120 30 254 0" fill="none" stroke="var(--lime)" stroke-width="4"/>
      <path d="M0 45 Q130 34 254 6" fill="none" stroke="var(--navy)" stroke-width="2"/>
    </svg>
    <p class="abs eoe">Clear Meadow Cleaning Services is an<br>Equal Opportunity Employer.</p>
    <div class="footer">www.clearmeadowcleanings.example</div>
  </section>

  <!-- Panel: back -->
  <section class="panel middle">
    <blockquote class="testimonial t1">
      <div class="mark" aria-hidden="true"><svg width="30" height="28" viewBox="0 0 30 28"><path d="M2 26V15C2 7 6 3 12 2l1 4c-3 1-5 3-5 7h5v13z M17 26V15c0-8 4-12 10-13l1 4c-3 1-5 3-5 7h5v13z" fill="var(--quote-mark)"/></svg></div>
      Clear Meadow Cleaning Services does an awesome job of cleaning our place and Tobias brings a sense of pride and professionalism each time he visits.
      <span class="who">Marla Penwick</span><span class="where">Brookvale, DE</span>
    </blockquote>
    <blockquote class="testimonial t2">
      <div class="mark" aria-hidden="true"><svg width="30" height="28" viewBox="0 0 30 28"><path d="M2 26V15C2 7 6 3 12 2l1 4c-3 1-5 3-5 7h5v13z M17 26V15c0-8 4-12 10-13l1 4c-3 1-5 3-5 7h5v13z" fill="var(--quote-mark)"/></svg></div>
      Clear Meadow Cleaning Services cleans our business as well as our home. Always a great job. Great and friendly service all the time. I recommend Clear Meadow to everyone.
      <span class="who">Dorian Ashgrove</span><span class="where">Linden Hollow, PA</span>
    </blockquote>
    <svg class="middle-lower" width="254" height="292" viewBox="0 0 254 292" aria-hidden="true">
      <path d="M0 46 Q120 20 254 6 L254 292 L0 292 Z" fill="var(--paper)"/>
      <path d="M0 40 Q110 12 254 2" fill="none" stroke="var(--lime)" stroke-width="5"/>
      <path d="M0 46 Q120 20 254 6" fill="none" stroke="var(--cyan)" stroke-width="1.5"/>
    </svg>
    <div class="abs middle-brand"><span class="brand"><i class="brand-dot"></i><span>Clear Meadow<br>Cleaning Services</span></span></div>
    <p class="abs queries">If you have any queries,<strong>Get in touch <em>with us</em></strong></p>
    <div class="abs icon-row" style="top:457px"><svg width="14" height="14" viewBox="0 0 16 16"><circle cx="8" cy="8" r="8" fill="var(--lime)"/><path d="M8 3.5a2.8 2.8 0 0 0-2.8 2.8C5.2 8.5 8 12 8 12s2.8-3.5 2.8-5.7A2.8 2.8 0 0 0 8 3.5z" fill="#fff"/><circle cx="8" cy="6.3" r="1" fill="var(--lime)"/></svg></div>
    <p class="abs address">48 Harlow Brook Lane<br>Millbridge, DE 19700</p>
    <div class="abs icon-row" style="top:510px"><svg width="14" height="14" viewBox="0 0 16 16"><circle cx="8" cy="8" r="8" fill="var(--lime)"/><path d="M5.3 4.3l1.4-.3.8 2-1 .7c.4 1 1.2 1.8 2.2 2.2l.7-1 2 .8-.3 1.4c-3 .3-6-2.7-5.8-5.8z" fill="#fff"/></svg></div>
    <p class="abs middle-phone">555.014.7290</p>
    <div class="footer footer--lime">www.clearmeadowcleanings.example</div>
  </section>

  <!-- Panel: cover -->
  <section class="panel panel--cover">
    <div class="abs cover-brand"><span class="brand"><i class="brand-dot"></i><span>Clear Meadow<br>Cleaning Services<span class="brand-sub">We enjoy doing the dirty work</span></span></span></div>
    <p class="abs tagline">It's not clean unless it's Clear Meadow clean</p>
    <div class="photo cover-photo" role="img" aria-label="Photo of a cleaner in blue gloves wiping a surface with a spray bottle"></div>
    <svg class="abs" style="top:118px" width="254" height="40" viewBox="0 0 254 40" aria-hidden="true">
      <path d="M0 10 Q120 40 254 14 L254 0 L0 0 Z" fill="var(--paper)"/>
      <path d="M0 12 Q120 42 254 16" fill="none" stroke="var(--lime)" stroke-width="4"/>
      <path d="M0 6 Q120 36 254 10" fill="none" stroke="var(--navy)" stroke-width="3"/>
    </svg>
    <svg class="abs" style="top:350px" width="254" height="45" viewBox="0 0 254 45" aria-hidden="true">
      <path d="M0 22 Q140 50 254 0 L254 45 L0 45 Z" fill="var(--paper)"/>
      <path d="M0 22 Q140 50 254 0" fill="none" stroke="var(--lime)" stroke-width="4"/>
      <path d="M0 28 Q140 54 254 6" fill="none" stroke="var(--navy)" stroke-width="2"/>
    </svg>
    <h1 class="banner">COMMERCIAL AND<br>RESIDENTIAL CLEANING</h1>
    <p class="abs about">We are a full service cleaning company that offers a full range of quality cleaning services to fit your needs no matter the size. We offer commercial and residential cleaning services to fit any size property. We take pride in doing your dirty work.</p>
    <p class="abs call-us">Call Us Today!</p>
    <p class="abs big-phone"><svg width="18" height="18" viewBox="0 0 16 16"><circle cx="8" cy="8" r="8" fill="var(--green)"/><path d="M5.3 4.3l1.4-.3.8 2-1 .7c.4 1 1.2 1.8 2.2 2.2l.7-1 2 .8-.3 1.4c-3 .3-6-2.7-5.8-5.8z" fill="#fff"/></svg>555.014.7290</p>
    <div class="footer">www.clearmeadowcleanings.example</div>
  </section>

</main>
</body>
</html>
```